Semi Permanent make up flyer

Hi

I will be sending a few thousand flyers dropped door to door in some very lovely parts of London.

The flyer must contain the following information;

New studio in Greenwich

Velmira Lineo trained technician - gold advanced level

Free consultation no obligation

Price List;
Eyebrow hair stroke: £325
Eyebrows 3D effect: £395
Microblading hair stroke: £330
Eyelash enhancement Top: £250
Eyelash enhancement Top & Bottom: £300
Lip blush: £450

Tel;……………….
Facebook: Odelie Permanent Cosmetics
Instagram: Odelie_Permanent_Cosmetics

Special introductory offers - available for a limited time only;
Like & share my page for 10% off any treatment
Refer a friend for £50 off each
Buy one treatment get 50% off another

I would like it to look clean, professional, expensive, and high end/luxury

I’m happy to make this a double sided print so I can have my logo on the front and the information on the back.

It must include my logo.

If you could use images of appealing women I think it would work best. Images have to have nice eyes, lips and brows. Weather you use entire face or features that is up to you.

Please show me a selection of different colour ways across the whole design. I personally feel softer tones would work. No black or bright colours.

I will be getting my new phone number in the next few days. I will let you know via messages what it is for you to add it in.

Any questions feel free to ask.

Target Market(s)

Women

Industry/Entity Type

Beauty Salon

Font styles to use
Sans Serif

Requirements
Must have
• Everything in Description
Nice to have
• The designers give their ideas. Im looking for input
Should not have
• Childish, cheap images or fonts. This is very high end so needs to look it

```html
<!DOCTYPE html>
<html lang="en">
<head>
<meta charset="utf-8">
<title>Odelie Permanent Cosmetics – Flyer</title>
<link rel="stylesheet" href="https://fonts.googleapis.com/css2?family=Roboto:wght@300;400;500;700&display=swap">
<style>
  :root {
    --backdrop: #141414;
    --paper: #ffffff;
    --gold: #c29a3c;
    --gold-deep: #b48a2c;
    --gold-light: #e6c86a;
    --gold-pale: #f3dc8c;
    --ink: #2e2e2e;
    --ink-soft: #5a5a5a;
    --hair: #8a4a2e;
    --skin: #ecc9b4;
    --skin-light: #f8e6dc;
  }
  * { box-sizing: border-box; margin: 0; padding: 0; }
  html, body { width: 1200px; height: 1200px; overflow: hidden; background: var(--backdrop); }
  body { position: relative; font-family: "Roboto", Arial, sans-serif; }

  .flyer { position: absolute; left: 185px; width: 806px; height: 572px; background: var(--paper); overflow: hidden; }
  .flyer--front { top: 22px; }
  .flyer--back { top: 607px; }

  .abs { position: absolute; }
  .center { text-align: center; }

  .brand { text-align: center; color: var(--gold); font-weight: 400; }
  .brand__mark { width: 90px; height: 90px; border-radius: 50%; background: var(--gold); margin: 0 auto 22px; }
  .brand__name { font-size: 22px; letter-spacing: 14px; text-indent: 14px; line-height: 22px; color: var(--ink-soft); }
  .brand__sub { font-size: 11px; letter-spacing: 2.6px; margin-top: 6px; }

  .social-band { position: absolute; left: 0; top: 512px; width: 806px; height: 33px;
    background: linear-gradient(90deg, var(--gold-deep) 0%, var(--gold-light) 50%, var(--gold) 100%);
    color: #fff; font-size: 14.5px; }
  .social { position: absolute; top: 8px; display: flex; align-items: center; gap: 8px; white-space: nowrap; }
  .social__dot { width: 10px; height: 10px; border-radius: 50%; background: #fff; }

  /* front */
  .hero-photo { left: 0; top: 0; width: 600px; height: 572px;
    background:
      radial-gradient(ellipse 320px 150px at 240px 30px, rgba(138,74,46,.95) 0%, rgba(138,74,46,.6) 45%, rgba(138,74,46,0) 100%),
      radial-gradient(ellipse 120px 260px at 0px 200px, rgba(110,58,36,.85) 0%, rgba(110,58,36,0) 100%),
      radial-gradient(ellipse 360px 420px at 300px 300px, var(--skin) 0%, var(--skin-light) 60%, rgba(255,255,255,0) 100%),
      linear-gradient(90deg, #e2b8a2 0%, var(--skin-light) 55%, #ffffff 100%); }
  .front-logo { left: 480px; top: 48px; width: 220px; }
  .front-copy { left: 366px; width: 440px; }
  .front-copy__headline { top: 282px; font-size: 26px; color: var(--gold); }
  .front-copy__services { top: 318px; font-size: 24px; color: var(--ink-soft); }
  .front-copy__body { top: 348px; font-size: 14px; line-height: 16px; color: var(--ink-soft); padding: 0 32px; }
  .front-copy__offer { top: 439px; font-size: 17.5px; color: var(--gold); }
  .front-copy__phone { top: 460px; font-size: 29px; font-weight: 700; color: var(--ink-soft); }

  /* back */
  .info-panel { left: 400px; top: 0; width: 406px; height: 572px; background: var(--gold); color: #fff; }
  .back-logo { left: 105px; top: 37px; width: 200px; }
  .feature-strip { left: 12px; top: 216px; width: 404px; height: 129px; display: flex; gap: 2px; }
  .feature-photo { flex: 1; height: 100%; }
  .feature-photo--lips { background:
      radial-gradient(ellipse 90px 45px at 100px 62px, #e88a78 0%, #d0685a 55%, rgba(120,60,50,0) 100%),
      linear-gradient(180deg, #8a6a60, #b07a6c 50%, #7a5a52); }
  .feature-photo--eye { background:
      radial-gradient(circle 24px at 85px 70px, #6f8a52 0%, #4c6b3c 60%, rgba(40,40,50,.9) 100%),
      linear-gradient(180deg, #b7b2c6 0%, #9a98b0 45%, #3a3a48 58%, #c6bfc8 100%); }
  .strip-tab { background: var(--gold-light); top: 237px; height: 82px; }
  .back-consult { left: 0; top: 396px; width: 400px; font-size: 17px; color: var(--ink); }
  .back-phone { left: 0; top: 425px; width: 400px; font-size: 42px; font-weight: 700; color: var(--gold); }

  .info__studio { top: 48px; width: 406px; font-size: 15px; }
  .info__tech { top: 81px; width: 406px; font-size: 15px; line-height: 16px; }
  .info__tech b { font-weight: 700; }
  .info__rule { top: 129px; left: 70px; width: 290px; height: 1px; background: linear-gradient(90deg, transparent, #8a6a20, transparent); }
  .price-box { top: 188px; left: 33px; width: 340px; height: 180px;
    box-shadow: inset 0 0 24px rgba(140,100,20,.35); }
  .price-tab { top: 237px; left: 372px; width: 34px; height: 82px; background: var(--gold-light); }
  .price-title { top: 143px; left: 70px; font-size: 23px; font-weight: 400; color: var(--ink); }
  .price-list { top: 194px; left: 55px; width: 275px; list-style: none; font-size: 16px; }
  .price-list li { display: flex; justify-content: space-between; align-items: flex-end; line-height: 20px; margin-bottom: 5.5px; padding-left: 13px; position: relative; }
  .price-list li::before { content: ""; position: absolute; left: 0; top: 8px; width: 6px; height: 6px; border-radius: 50%; background: var(--ink); }
  .offers__title { top: 381px; width: 406px; font-size: 21px; font-weight: 700; color: var(--gold-pale); }
  .offers__sub { top: 405px; width: 406px; font-size: 16.5px; font-weight: 700; color: var(--gold-pale); }
  .offers__item { width: 406px; font-size: 14px; color: var(--ink); }
  .offers__item b { font-size: 19px; font-weight: 700; }
</style>
</head>
<body>

<section class="flyer flyer--front">
  <div class="abs hero-photo" role="img" aria-label="Portrait photo of a smiling woman with short auburn hair resting her cheek on her hand"></div>

  <div class="abs brand front-logo">
    <div class="brand__mark"></div>
    <div class="brand__name">ODELIE</div>
    <div class="brand__sub">PERMANENT COSMETICS</div>
  </div>

  <p class="abs center front-copy front-copy__headline">New studio in Greenwich</p>
  <p class="abs center front-copy front-copy__services">SPA, BEAUTY &amp; PERSONAL CARE</p>
  <p class="abs center front-copy front-copy__body">Semi Permanent make up artist specialising in eyebrows, eyeliner and lips. Micropigmentation is used to create a natural more defined subtle make up effect</p>
  <p class="abs center front-copy front-copy__offer">Free consultation no obligation</p>
  <p class="abs center front-copy front-copy__phone">+44 7700 900123</p>

  <div class="social-band">
    <div class="social" style="left:308px;"><span class="social__dot"></span>Odelie Permanent Cosmetics</div>
    <div class="social" style="left:546px;"><span class="social__dot"></span>Odelie_Permanent_Cosmetics</div>
  </div>
</section>

<section class="flyer flyer--back">
  <div class="abs info-panel">
    <p class="abs center info__studio">NEW STUDIO IN GREENWICH</p>
    <p class="abs center info__tech">VELMIRA LINEO TRAINED TECHNICIAN -<br><b>GOLD ADVANCED LEVEL</b></p>
    <div class="abs info__rule"></div>
    <div class="abs price-box"></div>
    <div class="abs price-tab"></div>
    <h2 class="abs price-title">Price List</h2>
    <ul class="abs price-list">
      <li><span>Eyebrow hair stroke</span><span>£325</span></li>
      <li><span>Eyebrows 3D effect</span><span>£395</span></li>
      <li><span>Microblading hair stroke</span><span>£330</span></li>
      <li><span>Eyelash enhancement Top</span><span>£250</span></li>
      <li><span>Eyelash enhancement<br>Top &amp; Bottom</span><span>£300</span></li>
      <li><span>Lip blush</span><span>£450</span></li>
    </ul>
    <p class="abs center offers__title">SPECIAL INTRODUCTORY OFFERS</p>
    <p class="abs center offers__sub">available for a limited time only</p>
    <p class="abs center offers__item" style="top:430px;">Like &amp; share my page for <b>10%</b> off any treatment</p>
    <p class="abs center offers__item" style="top:454px;">Refer a friend for <b>£50</b> off each</p>
    <p class="abs center offers__item" style="top:478px;">Buy one treatment get <b>50%</b> off another</p>
  </div>

  <div class="abs brand back-logo">
    <div class="brand__mark"></div>
    <div class="brand__name">ODELIE</div>
    <div class="brand__sub">PERMANENT COSMETICS</div>
  </div>

  <div class="abs strip-tab" style="left:0;width:12px;"></div>
  <div class="abs strip-tab" style="left:416px;width:18px;"></div>
  <div class="abs feature-strip">
    <div class="feature-photo feature-photo--lips" role="img" aria-label="Close-up photo of lips with coral lip blush"></div>
    <div class="feature-photo feature-photo--eye" role="img" aria-label="Close-up photo of a green eye with defined eyeliner"></div>
  </div>

  <p class="abs center back-consult">Free consultation no obligation</p>
  <p class="abs center back-phone">+44 7700 900123</p>

  <div class="social-band">
    <div class="social" style="left:308px;"><span class="social__dot"></span>Odelie Permanent Cosmetics</div>
    <div class="social" style="left:546px;"><span class="social__dot"></span>Odelie_Permanent_Cosmetics</div>
  </div>
</section>

</body>
</html>
```